Small holiday retreat needs new Internet launch

"The Evolution from a Ruin into a Holiday Retreat.
My wife and I rebuilt a small farm in a remote village into a little holiday retreat. Though close to the Baltic Sea, we want to attract people with the desire to spend some days in a secluded place. Though remote it offers some luxury - and time ticks slower.
This summer was our third season and we want to adapt our Internet pages. Look at our business card - we want to keep this style.
It should be a bit mystic and should not attract the bargain hunter.
We realized that in summer our name "Wiesenkrone" (ie sunny hill) does not fit for the dark part of the year - then it is more like "Glimmering Moors".
We have a guesthouse (the former stable) and two tiny houses. Additionally, we have lavatory with sauna in the rebuilt barn and a fitness room.
On our farm live a few animals (dog, cats, chicken, bees) + wild visitors.
Our current home page is www.wiesenkrone-example.net
A few pictures are on Mapvista Atlas and I can share more in Cloudkeep Vault.
The final homepage should also offer translations into English, French, Dutch.
Better and consistent fonts.
No "galery" but more "four seasons".

Target Market(s)

Individual travellers - not just from Germany!

Industry/Entity Type

Tourism

Coding

Coded - Design and coding required

Number of Pages Required

4 page

Font styles to use
Script

Colors
FFC000
F8CF3A
FAE287
FDF2CF
FEFAEE

Requirements
Must have
• A "mystic" and romantic appearance.
Nice to have
• See my comments.

```html
<!DOCTYPE html>
<html lang="en">
<head>
<meta charset="utf-8">
<title>Wiesenkrone – Holiday Retreat</title>
<link rel="stylesheet" href="https://fonts.googleapis.com/css2?family=Jost:wght@400;500;600&family=Arimo:wght@400&display=swap">
<style>
:root{
  --orange:#f7860f;
  --brown:#6a4a28;
  --tan:#bb987a;
  --ink:#333;
  --muted:#666;
  --white:#fff;
  --line:#b9b9b9;
}
*{margin:0;padding:0;box-sizing:border-box}
html,body{width:1200px;height:4259px;overflow:hidden}
body{position:relative;background:var(--white);font-family:"Jost",sans-serif;color:var(--ink)}
.abs{position:absolute}
.center{left:0;width:1200px;text-align:center}

/* top bar */
.topbar{top:0;left:0;width:1200px;height:53px;background:var(--brown)}
.social{display:flex;gap:6px}
.social span{width:26px;height:26px;border:1.5px solid var(--white);border-radius:50%;display:block}
.topbar .social{position:absolute;left:111px;top:13px}
.topbar .contact-line{position:absolute;right:111px;top:15px;color:var(--white);font-size:16px;display:flex;gap:14px;align-items:center}
.topbar svg{vertical-align:-2px;margin-right:6px}

/* nav */
.nav{top:53px;left:0;width:1200px;height:117px;background:var(--white)}
.brand{position:absolute;display:flex;align-items:center;gap:12px;color:var(--orange);font-weight:500;font-size:34px}
.brand i{display:block;border-radius:50%;border:3px solid currentColor}
.nav .brand{left:111px;top:35px}
.nav .brand i{width:44px;height:44px}
.menu{position:absolute;left:432px;top:50px;display:flex;gap:30px;font-size:14px;font-weight:500;color:#444;text-transform:uppercase}
.menu .active{color:var(--orange)}
.menu .lang{color:var(--orange)}

/* hero */
.hero{top:170px;left:0;width:1200px;height:810px;background:linear-gradient(180deg,#3f5fc5 0%,#6d8ad0 30%,#b8b6b0 52%,#e0a352 62%,#7a5a2a 75%,#4d4a24 100%)}
.hero-title{top:360px;font-size:44px;font-weight:500;color:var(--white);line-height:70px;letter-spacing:.5px}
.btn{display:inline-block;background:var(--orange);color:var(--white);border-radius:30px;text-transform:uppercase;font-weight:500;text-align:center}
.hero-btn{position:absolute;left:500px;top:514px;width:200px;height:61px;line-height:61px;font-size:20px}
.dots{left:1118px;top:773px;display:flex;flex-direction:column;gap:7px}
.dots span{width:13px;height:13px;border-radius:50%;background:var(--white)}
.dots span.on{background:var(--orange)}

/* welcome */
.portrait{left:130px;top:1021px;width:430px;height:430px;border-radius:50%;background:radial-gradient(circle at 45% 40%,#c9a48a,#8a5a3d 60%,#5a3b28);border:5px solid transparent;border-right-color:var(--orange);border-bottom-color:var(--orange);transform:rotate(10deg)}
.welcome h2{left:616px;top:1028px;font-size:23px;font-weight:500;line-height:42px;color:var(--brown);text-transform:uppercase}
.welcome h2 em{font-style:normal;color:var(--orange)}
.welcome p{left:616px;top:1127px;width:439px;font-family:"Arimo",sans-serif;font-size:13px;line-height:26.5px;color:var(--muted);text-align:justify}
.welcome .btn{position:absolute;left:615px;top:1393px;width:155px;height:53px;line-height:53px;font-size:16px}

/* seasons */
.seasons-band{top:1529px;left:0}
.section-title{font-size:40px;font-weight:500;text-transform:uppercase}
.rule{width:46px;height:3px;margin:14px auto 0}
.seasons .section-title{color:var(--white);top:1596px}
.seasons .rule{background:var(--white)}
.season{top:1716px;width:192px;text-align:center}
.season .disc{width:192px;height:192px;border-radius:50%;border:5px solid var(--white)}
.season b{display:block;margin-top:17px;font-size:24px;font-weight:500;color:var(--white)}

/* retreats */
.retreats .section-title{top:2140px;color:var(--ink);font-size:34px}
.retreats .rule{background:var(--orange)}
.card{top:2233px;width:313px;text-align:center}
.card .photo{height:273px}
.card .label{margin:-30px 12px 0;background:var(--white);padding-top:16px;border-radius:6px 6px 0 0;position:relative}
.card h3{font-size:20px;font-weight:500;color:var(--ink);line-height:31px}
.card h4{font-size:20px;font-weight:500;color:var(--orange);line-height:31px}
.card p{font-family:"Arimo",sans-serif;font-size:14px;line-height:26px;color:var(--muted);margin-top:4px}
.btn-outline{display:inline-block;margin-top:20px;width:137px;height:43px;line-height:41px;border:1.5px solid var(--orange);border-radius:22px;color:var(--orange);font-size:15px;font-weight:500}

/* bookings */
.bookings-band{top:2752px;left:0}
.bookings .section-title{top:2854px;color:var(--white)}
.bookings .rule{background:var(--white)}
.field{top:2962px;width:243px}
.field label{display:block;font-size:15px;font-weight:500;color:var(--white);text-transform:uppercase;padding-left:13px;margin-bottom:12px}
.field .box{height:47px;background:var(--white);border-radius:24px;padding:0 16px;display:flex;align-items:center;justify-content:space-between;font-size:15px;color:#555}
.bookings .btn{position:absolute;left:501px;top:3085px;width:198px;height:51px;line-height:51px;font-size:18px}

/* contact */
.contact .section-title{top:3287px;font-size:34px;color:var(--ink)}
.contact .rule{background:var(--orange)}
.touch{left:136px;top:3392px;font-size:30px;font-weight:400;line-height:43px;color:var(--ink)}
.phone{left:136px;top:3490px;display:flex;gap:14px;align-items:center}
.phone .ring{width:52px;height:52px;border-radius:50%;border:2px solid #f4c99a;display:flex;align-items:center;justify-content:center}
.phone small{display:block;font-size:15px;color:var(--muted)}
.phone strong{display:block;font-size:25px;font-weight:500;letter-spacing:.5px}
.info{left:140px;display:flex;gap:10px}
.info .tick{width:16px;height:16px;border-radius:50%;background:var(--orange);margin-top:4px;display:flex;align-items:center;justify-content:center}
.info b{display:block;font-size:19px;font-weight:500;text-decoration:underline}
.info span{display:block;font-family:"Arimo",sans-serif;font-size:13px;color:var(--muted);margin-top:12px}
.form label{position:absolute;font-size:13px;font-weight:500;color:#444;text-transform:uppercase}
.form .input{position:absolute;border:1.5px solid var(--line);background:var(--white)}
.form .btn{position:absolute;left:534px;top:3700px;width:127px;height:38px;line-height:38px;font-size:15px}

/* footer */
.footer-band{top:3730px;left:0}
.footer .brand{left:0;width:1200px;justify-content:center;top:3920px;color:var(--white);font-size:44px}
.footer .brand i{width:90px;height:90px}
.foot-menu{top:4072px;display:flex;justify-content:center;gap:34px;font-size:14px;font-weight:500;color:var(--white);text-transform:uppercase}
.footer .social{top:4128px;left:0;width:1200px;justify-content:center;gap:8px}
.footer .social span{width:36px;height:36px}
.copy{top:4190px;font-size:14px;color:var(--white)}
</style>
</head>
<body>

<header class="abs topbar">
  <div class="social"><span></span><span></span><span></span><span></span><span></span></div>
  <div class="contact-line">
    <span><svg width="14" height="14" viewBox="0 0 24 24"><path fill="#fff" d="M6.6 10.8a15 15 0 0 0 6.6 6.6l2.2-2.2a1 1 0 0 1 1-.25 11.4 11.4 0 0 0 3.6.57 1 1 0 0 1 1 1V20a1 1 0 0 1-1 1A17 17 0 0 1 3 4a1 1 0 0 1 1-1h3.5a1 1 0 0 1 1 1c0 1.25.2 2.45.57 3.57a1 1 0 0 1-.25 1z"/></svg>Call Us : +49 1520 4477 318</span>
    <span style="opacity:.6">|</span>
    <span><svg width="16" height="13" viewBox="0 0 24 18"><path fill="#fff" d="M0 0h24v18H0zM2 2v1l10 7 10-7V2z"/></svg>Email : post@anna-lindqvist.example</span>
  </div>
</header>

<nav class="abs nav">
  <div class="brand"><i></i>Wiesenkrone</div>
  <div class="menu">
    <span class="active">Home</span><span>About Us</span><span>Accommodation</span><span>Calendar</span><span>Gallery</span><span>Contact <span style="color:#ccc">|</span> <span class="lang">EN ▾</span></span>
  </div>
</nav>

<section class="abs hero" role="img" aria-label="Photo of a sunset over wide green fields with a tree at the edge"></section>
<h1 class="abs center hero-title">THE EVOLUTION FROM<br>A RUIN INTO A HOLIDAY RETREAT</h1>
<a class="btn hero-btn">Learn More</a>
<div class="abs dots"><span></span><span class="on"></span><span></span></div>
<svg class="abs" style="top:780px;left:0" width="1200" height="200" viewBox="0 0 1200 200">
  <path fill="#fff" d="M0 104C250-20 500 120 800 178C1000 212 1100 175 1200 146V200H0Z"/>
  <path fill="var(--orange)" d="M30 100C250-12 520 132 790 170C880 180 940 178 985 172C720 168 470 76 30 100Z"/>
</svg>

<section class="welcome">
  <div class="abs portrait" role="img" aria-label="Photo of the host seated at a wooden table by a brick wall with candles"></div>
  <h2 class="abs">Welcome to <em>the Wiesenkrone</em><br><em>in beautiful Carinerland</em></h2>
  <p class="abs">Welcome to the Wiesenkrone in beautiful Carinerland. With great attention to detail, we have turned our old farm into a place of rest and relaxation. Whether in the tiny house "Kiesel" or the holiday apartments "Abendrot" and "Morgentau", in all of our accommodations we attach great importance to the fact that you as a guest immediately feel comfortable and that you arrive in the middle of an enchanted garden and in your time-out.In a quiet and idyllic location, you can still quickly reach the Hanseatic cities of Wismar and Rostock as well as the beaches of Kuehlungsborn, Salzhaff and Rerik.</p>
  <a class="btn">Read More</a>
</section>

<section class="seasons">
  <svg class="abs seasons-band" width="1200" height="560" viewBox="0 0 1200 560">
    <defs><linearGradient id="seasonFill" x1="0" y1="0" x2="0" y2="1"><stop offset="0" stop-color="#f98a12"/><stop offset=".6" stop-color="#f7860f"/><stop offset="1" stop-color="#ee8a2a"/></linearGradient></defs>
    <path fill="url(#seasonFill)" d="M0 83Q600-83 1200 83V455Q600 621 0 455Z"/>
  </svg>
  <div class="abs center section-title">Four Seasons<div class="rule"></div></div>
  <div class="abs season" style="left:142px"><div class="disc" role="img" aria-label="Photo of spring branches against blue sky" style="background:linear-gradient(160deg,#5a9ee0,#9cc3e8 60%,#6e7f3a)"></div><b>SPRING</b></div>
  <div class="abs season" style="left:385px"><div class="disc" role="img" aria-label="Photo of a summer sunset behind trees" style="background:linear-gradient(180deg,#d8b4cf,#f2b49a 55%,#5b3e30)"></div><b>SUMMER</b></div>
  <div class="abs season" style="left:628px"><div class="disc" role="img" aria-label="Photo of the farmhouse in an autumn garden" style="background:linear-gradient(180deg,#a9c4e6,#c79a5a 50%,#6a7a3a)"></div><b>AUTUMN</b></div>
  <div class="abs season" style="left:871px"><div class="disc" role="img" aria-label="Photo of snowy trees and a tiny house in winter" style="background:linear-gradient(180deg,#8aa7d8,#d7e0f0 55%,#f2f4f8)"></div><b>WINTER</b></div>
</section>

<section class="retreats">
  <div class="abs center section-title">Rental Retreats<div class="rule"></div></div>
  <div class="abs card" style="left:111px"><div class="photo" role="img" aria-label="Photo of a rustic dining room with brick wall and set table" style="background:linear-gradient(180deg,#6a4a30,#9a7050 50%,#4a3424)"></div><div class="label"><h3>DESIGN REFUGE</h3><h4>"ABENDROT"</h4><p>Historical elements with contemporary<br>characterize this feel-good loft.</p><a class="btn-outline">READ MORE</a></div></div>
  <div class="abs card" style="left:443px"><div class="photo" role="img" aria-label="Photo of a loft bedroom under wooden beams" style="background:linear-gradient(180deg,#8a7a6a,#c8bcae 45%,#7a6a5a)"></div><div class="label"><h3>DESIGN REFUGE</h3><h4>"MORGENTAU"</h4><p>Historical elements with contemporary<br>characterize this feel-good loft.</p><a class="btn-outline">READ MORE</a></div></div>
  <div class="abs card" style="left:775px"><div class="photo" role="img" aria-label="Photo of a tiny house kitchen with timber frame" style="background:linear-gradient(180deg,#b08060,#d8c8b8 45%,#8a6a4a)"></div><div class="label"><h3>TINY HOUSE</h3><h4>"BIRKE"</h4><p>Historical elements with contemporary<br>characterize this feel-good loft.</p><a class="btn-outline">READ MORE</a></div></div>
</section>

<section class="bookings">
  <svg class="abs bookings-band" width="1200" height="475" viewBox="0 0 1200 475">
    <path fill="var(--tan)" d="M0 83Q600-83 1200 83V380Q600 560 0 380Z"/>
  </svg>
  <div class="abs center section-title">Bookings &amp; Calendar<div class="rule"></div></div>
  <div class="abs field" style="left:215px"><label>Arrival</label><div class="box">04.10.22<svg width="14" height="14" viewBox="0 0 14 14"><rect x="1" y="2" width="12" height="11" fill="none" stroke="#999"/><path d="M1 5h12" stroke="#999"/></svg></div></div>
  <div class="abs field" style="left:479px"><label>Departure</label><div class="box">04.10.22<svg width="14" height="14" viewBox="0 0 14 14"><rect x="1" y="2" width="12" height="11" fill="none" stroke="#999"/><path d="M1 5h12" stroke="#999"/></svg></div></div>
  <div class="abs field" style="left:742px"><label>Persons</label><div class="box">01<svg width="10" height="6" viewBox="0 0 10 6"><path d="M0 0h10L5 6z" fill="#555"/></svg></div></div>
  <a class="btn">Search</a>
</section>

<section class="contact">
  <div class="abs center section-title">Contact Us<div class="rule"></div></div>
  <h3 class="abs touch">Get in Touch &amp; Let’s<br>Get Started.</h3>
  <div class="abs phone">
    <div class="ring"><svg width="26" height="26" viewBox="0 0 24 24"><path fill="var(--orange)" d="M6.6 10.8a15 15 0 0 0 6.6 6.6l2.2-2.2a1 1 0 0 1 1-.25 11.4 11.4 0 0 0 3.6.57 1 1 0 0 1 1 1V20a1 1 0 0 1-1 1A17 17 0 0 1 3 4a1 1 0 0 1 1-1h3.5a1 1 0 0 1 1 1c0 1.25.2 2.45.57 3.57a1 1 0 0 1-.25 1z"/></svg></div>
    <div><small>Phone Number</small><strong>+49 152 044 773 18</strong></div>
  </div>
  <div class="abs info" style="top:3582px"><div class="tick"><svg width="9" height="9" viewBox="0 0 10 10"><path d="M1 5l3 3 5-6" fill="none" stroke="#fff" stroke-width="2"/></svg></div><div><b>Address:</b><span>Am Wiesenrand 7, 18299 Feldmark, Germany</span></div></div>
  <div class="abs info" style="top:3654px"><div class="tick"><svg width="9" height="9" viewBox="0 0 10 10"><path d="M1 5l3 3 5-6" fill="none" stroke="#fff" stroke-width="2"/></svg></div><div><b>Email :</b><span>post@anna-lindqvist.example</span></div></div>
  <div class="form">
    <label style="left:534px;top:3404px">First Name</label><div class="input" style="left:534px;top:3425px;width:255px;height:35px"></div>
    <label style="left:820px;top:3404px">Last Name</label><div class="input" style="left:820px;top:3425px;width:254px;height:35px"></div>
    <label style="left:534px;top:3484px">Email</label><div class="input" style="left:534px;top:3506px;width:255px;height:35px"></div>
    <label style="left:820px;top:3484px">Phone</label><div class="input" style="left:820px;top:3506px;width:254px;height:35px"></div>
    <label style="left:534px;top:3561px">Message</label><div class="input" style="left:534px;top:3580px;width:540px;height:100px"></div>
    <a class="btn">Submit</a>
  </div>
</section>

<footer class="footer">
  <svg class="abs footer-band" width="1200" height="529" viewBox="0 0 1200 529">
    <path fill="var(--brown)" d="M0 112C300 44 500 138 800 84C1000 48 1100 36 1200 28V529H0Z"/>
    <path fill="var(--orange)" d="M0 104C300 32 500 128 800 72C1000 36 1100 24 1200 20V30C1100 36 1000 48 800 84C500 138 300 44 0 112Z"/>
  </svg>
  <div class="brand"><i></i>Wiesenkrone</div>
  <nav class="abs center foot-menu"><span>Home</span><span>About Us</span><span>Accommodation</span><span>Calendar</span><span>Gallery</span><span>Contact</span></nav>
  <div class="abs social"><span></span><span></span><span></span><span></span><span></span></div>
  <p class="abs center copy">© Copyright 2022 Wiesenkrone.All Rights Reserved.</p>
</footer>

</body>
</html>
```